Business Card Design

Copperfield Lantern & Spark, Inc. (CLS), located in Memphis, TN began operating on 2003. We are a certified
minority woman-owned business that genuinely takes a vested interest in our customers. We serve utilities,
government, contractors and end user markets in electrical, water, gas and industrial supplies. Our core
competency as a distributor of electrical materials has positioned us to serve business of all size. As your supply
chain partner, we arm you with the resources you need to make your supply chain more efficient. Our team
works with your team on a daily basis to help you solve problems and achieve goals. This team approach has
helped CLS customers to succeed and we can do the same for you.

NAICS Codes:
423610 Electrical Apparatus and Equipment, Wiring Supplies, and Related Equipment Merchant
Wholesalers
423510 Metal Service Centers and Other Metal Merchant Wholesalers
423720 Plumbing and Heating Equipment and Supplies (Hydronics) Merchant Wholesalers

Certifications
MBE (KRVPQAL, State of Tennessee Up-MRX and FJW), WBE (HQOLT),
WOSB, DOT (TDOT, MDOT, ALDOT, SCDOT, NCDOT, and VDOT), LOSB,
SBE, and LSB Certified
Some of Our Products Include:
. Boxes & Covers
. Conduit & Raceway
. Fittings
. Fuses
. Lamp & Ballasts
. Lighting Controls & Timers
. Lighting Fixtures
. Personal Safety
. Pipes
. Power Distribution
. Terminations Ground & Splices
. Tools & Testers
. Wire, Cords & Cable
. Wiring Devices
. Valves

Industry/Entity Type

Business

Contact Information for Business Card

Marianne T. Holloway - President/CEO
4728 Quillon Ave., Memphis, TN 38127
901-555-0147 office, 901-555-0182 fax, 901-555-0163 cell
mtholloway@clsllc-example.com - www.clsincorp-example.com

```html
<!DOCTYPE html>
<html lang="en">
<head>
<meta charset="utf-8">
<title>Copperfield Lantern &amp; Spark – Business Card</title>
<link rel="stylesheet" href="https://fonts.googleapis.com/css2?family=Source+Sans+3:wght@400;600;700&display=swap">
<style>
  :root {
    --backdrop: #000000;
    --card: #3a3a3d;
    --card-edge: #2f2f32;
    --accent: #e4e82a;
    --text: #ffffff;
    --rule: #6f6f3a;
  }
  html, body {
    margin: 0;
    width: 1200px;
    height: 900px;
    overflow: hidden;
    background: var(--backdrop);
    font-family: "Source Sans 3", sans-serif;
    color: var(--text);
  }
  .canvas { position: relative; width: 1200px; height: 900px; }
  .card {
    position: absolute;
    top: 271px;
    width: 456px;
    height: 281px;
    border-radius: 14px;
    background: radial-gradient(ellipse at 50% 45%, #414144 0%, var(--card) 55%, var(--card-edge) 100%);
    overflow: hidden;
  }
  .card--front { left: 137px; }
  .card--back { left: 626px; }
  .divider {
    position: absolute;
    width: 1px;
    background: linear-gradient(to bottom, transparent, var(--rule) 20%, var(--rule) 80%, transparent);
  }
  .card--front .divider { left: 253px; top: 38px; height: 206px; }
  .card--back .divider { left: 189px; top: 30px; height: 220px; }

  .wordmark {
    position: absolute;
    left: 24px;
    top: 112px;
    display: flex;
    align-items: center;
    gap: 10px;
  }
  .wordmark__dot {
    width: 12px; height: 12px; border-radius: 50%;
    background: var(--accent);
    flex: none;
  }
  .wordmark__name {
    font-size: 22px;
    font-weight: 600;
    line-height: 1.1;
    color: var(--text);
  }

  .contact { position: absolute; left: 266px; top: 41px; }
  .contact__name { margin: 0; font-size: 17.5px; font-weight: 700; color: var(--accent); line-height: 1.2; }
  .contact__title { margin: 4px 0 0; font-size: 13px; line-height: 1.2; }
  .contact__address { margin: 16px 0 0; font-size: 13px; line-height: 18px; font-style: normal; }
  .contact__list { list-style: none; margin: 12px 0 0; padding: 0; }
  .contact__item { display: flex; align-items: center; height: 19px; font-size: 13px; }
  .contact__item--long { font-size: 11px; }
  .contact__icon { width: 10px; height: 10px; margin: 0 9px 0 2px; flex: none; fill: var(--accent); }

  .mark {
    position: absolute;
    left: 62px;
    top: 110px;
    display: flex;
    align-items: center;
    gap: 12px;
  }
  .mark__dot {
    width: 22px; height: 22px; border-radius: 50%;
    background: radial-gradient(circle, #f2f55a 0%, var(--accent) 60%, #b7b82a 100%);
  }
  .mark__name { font-size: 46px; font-weight: 700; line-height: 1; color: var(--text); }

  .products {
    position: absolute;
    left: 219px;
    top: 18px;
    list-style: none;
    margin: 0; padding: 0;
  }
  .products__item {
    position: relative;
    padding-left: 17px;
    font-size: 12.5px;
    font-weight: 600;
    line-height: 16.4px;
  }
  .products__item::before {
    content: "";
    position: absolute;
    left: 0; top: 4px;
    width: 8px; height: 8px; border-radius: 50%;
    background: radial-gradient(circle, #f4f66a 0%, var(--accent) 55%, #8e8f22 100%);
  }
</style>
</head>
<body>
<main class="canvas">
  <section class="card card--front" aria-label="Card front">
    <div class="wordmark">
      <span class="wordmark__dot"></span>
      <span class="wordmark__name">Copperfield<br>Lantern &amp; Spark</span>
    </div>
    <div class="divider"></div>
    <div class="contact">
      <h1 class="contact__name">Marianne T. Holloway</h1>
      <p class="contact__title">President/CEO</p>
      <address class="contact__address">4728 Quillon Ave.,<br>Memphis, TN 38127</address>
      <ul class="contact__list">
        <li class="contact__item">
          <svg class="contact__icon" viewBox="0 0 10 10"><path d="M2 0.5 L3.6 2.6 L2.8 3.6 Q4 6 6.4 7.2 L7.4 6.4 L9.5 8 L8.4 9.5 Q3.5 9 0.5 1.6 Z"/></svg>
          901-555-0147
        </li>
        <li class="contact__item">
          <svg class="contact__icon" viewBox="0 0 10 10"><path d="M2.5 0 H7.5 V10 H2.5 Z M3.5 1 V8 H6.5 V1 Z"/></svg>
          901-555-0163
        </li>
        <li class="contact__item">
          <svg class="contact__icon" viewBox="0 0 10 10"><path d="M2 0 H7 V3 H9 V10 H1 V3 H2 Z M3 4.5 V6 H7 V4.5 Z M3 7 V8.5 H7 V7 Z"/></svg>
          901-555-0182
        </li>
        <li class="contact__item contact__item--long">
          <svg class="contact__icon" viewBox="0 0 10 10"><path d="M0 2 H10 V8.5 H0 Z M0.8 2.6 L5 5.6 L9.2 2.6 Z" fill-rule="evenodd"/></svg>
          mtholloway@clsllc-example.com
        </li>
        <li class="contact__item contact__item--long">
          <svg class="contact__icon" viewBox="0 0 10 10"><circle cx="5" cy="5" r="4.6"/></svg>
          www.clsincorp-example.com
        </li>
      </ul>
    </div>
  </section>

  <section class="card card--back" aria-label="Card back">
    <div class="mark">
      <span class="mark__dot"></span>
      <span class="mark__name">CLS</span>
    </div>
    <div class="divider"></div>
    <ul class="products">
      <li class="products__item">Boxes &amp; Covers</li>
      <li class="products__item">Conduit &amp; Raceway</li>
      <li class="products__item">Fittings</li>
      <li class="products__item">Fuses</li>
      <li class="products__item">Lamp &amp; Ballasts</li>
      <li class="products__item">Lighting Controls &amp; Timers</li>
      <li class="products__item">Lighting Fixtures</li>
      <li class="products__item">Personal Safety</li>
      <li class="products__item">Pipes</li>
      <li class="products__item">Power Distribution</li>
      <li class="products__item">Terminations Ground &amp; Splices</li>
      <li class="products__item">Tools &amp; Testers</li>
      <li class="products__item">Wire, Cords &amp; Cable</li>
      <li class="products__item">Wiring Devices</li>
      <li class="products__item">Valves</li>
    </ul>
  </section>
</main>
</body>
</html>
```